Realtor Website Design

We are working with KRV•DEL. They are a financial advising company that needs a new website design.

Some sites to use for inspiration:

https://www.morvathine.com
https://www.pildovanhomes.com

Thank you for taking the time to consider designing a website for us. We are web developers based in Stockton and Los Angeles, CA, USA. Most of our projects go through the same process. Understanding this process may help you win a project with us. We custom-code all of our websites in-house. We don’t have any requirements as to what tools you use for your design, but we prefer Figma files. For any design that we label as four-stars, we send it to the client for review. The client picks the final design they want us to use. Once we complete this process, we will continue to show additional clients all the four-star sites and purchase them later. Your designs will have multiple chances to sell. For better chances of success, we ask that you follow these guidelines.

IMAGES:
If you use any images or icons in the design, we ask that you have a link to the asset so we can purchase the image/icon. Most of the designs we submit do not have the customer’s images on them unless they have some great images. Be creative; show us the feeling you are trying to portray with your image choices. Use any royalty-free site you choose. We subscribe to Zentiq and mainly use their images, but we can purchase images outside of Zentiq.

PLEASE NOTE: we will not submit designs to clients with watermarks on the images.

FONTS:
We ask that you identify the fonts used in the design. This can be done in a message if you want. We typically use Google Fonts and Zentiq Fonts.

CONTENT:
We're always open to different content and ideas. We often submit designs with stock images so the client can see our vision. We typically take pictures after the website launch to use their images with our vision. Lorem Ipsum is fine for paragraphs, but we ask that you write the headers in correct English. We want to be able to show the vision and identify the sections of the website.

INSPIRATION:
We typically add a couple of links in the brief of websites we like to help you get started in your design.

REVISIONS:
We do not often ask for revisions of the designs unless we see something in the design that may not appeal to the client. If there are slight changes that we want to make, we do that in the development process.

FEEDBACK:
We rarely give feedback on designs during the design process. We are working on many website projects and do not have the time to provide feedback. We usually respond if your request is well thought out and asks specific questions, but a note asking “feedback, please” usually goes unanswered.

```html
<!DOCTYPE html>
<html lang="en">
<head>
<meta charset="utf-8">
<title>KRV•DEL — Financial Advisory</title>
<link href="https://fonts.googleapis.com/css2?family=Inter:wght@400;500;600&display=swap" rel="stylesheet">
<style>
:root{
  --teal:#0f9488;
  --teal-dark:#0b7d73;
  --mint:#d6f7ef;
  --ink:#111827;
  --navy:#111827;
  --navy-2:#1a2233;
  --muted:#6b7280;
  --body:#4b5563;
  --line:#e5e7eb;
  --panel:#f7f8fa;
  --white:#ffffff;
}
*{box-sizing:border-box;margin:0;padding:0}
html,body{width:1200px;height:5277px;overflow:hidden}
body{font-family:"Inter",Arial,sans-serif;color:var(--ink);background:var(--white);position:relative;font-size:13px;line-height:1.6}
.abs{position:absolute}
.tag{display:inline-block;background:var(--mint);color:var(--teal-dark);font-size:13px;padding:6px 14px;line-height:1.4}
.section-title{font-size:14px;font-weight:500;color:var(--ink)}
p{color:var(--body)}

.hero{position:absolute;left:0;top:0;width:1200px;height:770px;background:linear-gradient(120deg,#2c3547 0%,#3b4456 40%,#283041 70%,#1c2232 100%)}
.hero-shade{position:absolute;inset:0;background:linear-gradient(90deg,rgba(22,28,42,.75),rgba(22,28,42,.35))}
.nav{position:absolute;left:76px;right:76px;top:18px;height:34px;display:flex;align-items:center;justify-content:space-between}
.logo{color:#5eead4;font-size:20px;font-weight:500;display:flex;align-items:center;gap:8px}
.logo .dot{width:14px;height:14px;background:#5eead4;border-radius:50%}
.nav-links{display:flex;align-items:center;gap:30px;font-size:13px;color:#e5e7eb}
.btn{display:inline-flex;align-items:center;justify-content:center;background:var(--teal);color:#fff;font-size:12px;font-weight:500}
.nav .btn{padding:8px 14px}
.hero-copy{position:absolute;left:76px;top:290px;width:570px;color:#fff}
.hero-copy h1{font-size:13px;font-weight:400;margin-bottom:22px}
.hero-copy p{color:#f1f5f9;font-size:16px;line-height:1.55;margin-bottom:26px}
.hero-btns{display:flex;gap:16px}
.hero-btns .btn{width:198px;height:44px;border-radius:3px}
.btn-ghost{width:182px;height:44px;background:#fff;border-radius:3px}

.about-panel{left:76px;top:856px;width:545px;height:629px;background:var(--panel)}
.about-copy{left:76px;top:972px;width:490px}
.about-copy .tag{margin-bottom:24px}
.about-copy h2{font-size:13px;font-weight:500;margin-bottom:24px}
.about-copy p{font-size:12.5px;line-height:1.7;margin-bottom:14px}
.stats{display:flex;margin-top:6px;text-align:center}
.stat{width:176px}
.stat svg{display:block;margin:0 auto 6px}
.stat b{display:block;font-weight:400;font-size:13px}
.stat span{font-size:11px;color:var(--muted)}
.about-img{left:621px;top:856px;width:504px;height:629px;background:linear-gradient(160deg,#1f5a58 0%,#175450 45%,#2d3030 70%,#0f1214 100%)}
.quote-box{left:593px;top:1407px;width:283px;height:108px;background:var(--teal);color:#fff;font-size:13px;padding:28px 28px;line-height:1.55;box-shadow:0 10px 24px rgba(0,0,0,.15)}

.services-head{left:0;width:1200px;top:1655px;text-align:center}
.services-head .tag{margin-bottom:22px}
.services-head p{width:640px;margin:20px auto 0;font-size:13px}
.card{position:absolute;width:330px;border:1px solid var(--line);background:#fff;padding:30px 28px}
.icon-box{width:48px;height:48px;background:var(--mint);display:flex;align-items:center;justify-content:center;margin-bottom:38px}
.card h3{font-size:13px;font-weight:500;margin-bottom:40px}
.card p{font-size:12.5px;line-height:1.68}

.approach{left:76px;top:2615px;width:1049px;height:735px;background:var(--navy)}
.approach-img{left:76px;top:2783px;width:496px;height:398px;background:radial-gradient(ellipse at 40% 60%,#5a1d16 0%,#2a1210 45%,#0b0d0c 100%)}
.approach-copy{left:628px;top:2615px;width:470px;color:#fff}
.approach-copy .tag{background:var(--teal);color:#d1fae5;padding:4px 14px}
.approach-copy h2{font-size:13px;font-weight:500;margin:24px 0 26px}
.approach-copy .lead{color:#d1d5db;font-size:12.5px;line-height:1.7}
.step{position:absolute;left:628px;width:470px;display:flex;gap:22px}
.step .num{width:56px;height:56px;background:var(--teal);color:#fff;display:flex;align-items:center;justify-content:center;font-size:13px;flex:none}
.step h4{color:#fff;font-size:13px;font-weight:500;margin-bottom:8px}
.step p{color:#9ca3af;font-size:12.5px;line-height:1.7}
.fiduciary{left:628px;top:3232px;width:497px;height:118px;background:var(--navy-2);padding:22px 24px;display:flex;gap:12px}
.fiduciary h4{color:#fff;font-size:16px;font-weight:500;margin-bottom:10px}
.fiduciary p{color:#9ca3af;font-size:12.5px;line-height:1.7}

.testi-bg{left:32px;top:3500px;width:1136px;height:580px;background:#f9fafb}
.testi-head{left:0;width:1200px;top:3524px;text-align:center}
.testi-head .tag{margin-bottom:22px}
.testi-head p{width:640px;margin:20px auto 0;font-size:13px}
.tcard{position:absolute;top:3720px;width:330px;height:348px;background:#fff;border:1px solid var(--line);padding:28px 28px}
.stars{display:flex;gap:4px;margin-bottom:36px}
.tcard blockquote{font-style:italic;color:var(--body);font-size:12.5px;line-height:1.7;height:172px}
.tcard hr{border:0;border-top:1px solid var(--line);margin-bottom:18px}
.tcard .name{font-size:13px}
.tcard .role{font-size:11px;color:var(--muted)}

.contact-copy{left:76px;top:4240px;width:480px}
.contact-copy .tag{margin-bottom:22px}
.contact-copy h2{font-size:13px;font-weight:500;margin-bottom:22px}
.contact-copy .lead{font-size:12.5px;line-height:1.7;margin-bottom:30px}
.info{display:flex;gap:20px;margin-bottom:28px}
.info .ic{width:40px;height:40px;background:var(--mint);display:flex;align-items:center;justify-content:center;flex:none}
.info b{display:block;font-weight:400;font-size:13px}
.info span{color:var(--body);font-size:12.5px;line-height:1.6}
.hours{left:76px;top:4690px;width:496px;height:144px;background:var(--panel);padding:22px 22px}
.hours h4{font-size:16px;font-weight:500;margin-bottom:10px}
.hours p{font-size:12.5px;line-height:1.7}
.form{left:628px;top:4245px;width:497px;height:570px;background:var(--panel);padding:38px 42px}
.form h3{font-size:13px;font-weight:500;margin-bottom:26px}
.field{margin-bottom:20px}
.field label{display:block;font-size:11px;font-weight:500;margin-bottom:8px}
.field .input{height:32px;background:#eceef1;font-size:11px;color:#9ca3af;padding:8px 12px;line-height:1.4}
.field .area{height:130px}
.form .btn{width:100%;height:42px;margin-top:8px}

.footer{left:0;top:4900px;width:1200px;height:377px;background:var(--navy);color:#fff}
.f-brand{left:66px;top:55px;width:220px}
.f-brand p{color:#9ca3af;font-size:12.5px;line-height:1.7;margin-top:14px}
.socials{display:flex;gap:14px;margin-top:28px}
.socials span{width:30px;height:30px;border:1px solid #374151;display:block}
.f-col{top:60px;width:240px}
.f-col h4{font-size:16px;font-weight:500;margin-bottom:14px}
.f-col a{display:block;color:#e5e7eb;font-size:12.5px;text-decoration:none;margin-bottom:12px}
.f-col .dim{color:#9ca3af}
.f-bottom{left:66px;right:56px;top:280px;border-top:1px solid #1f2937;padding-top:24px;display:flex;justify-content:space-between;font-size:11px;color:#9ca3af}
.f-bottom nav{display:flex;gap:22px;color:#d1d5db}
</style>
</head>
<body>

<section class="hero" role="img" aria-label="Photo of financial advisors reviewing documents at a desk">
  <div class="hero-shade"></div>
</section>
<header class="nav">
  <div class="logo"><span class="dot"></span>Marlowe</div>
  <nav class="nav-links">
    <span>About</span><span>Services</span><span>Our Approach</span><span>Testimonials</span>
    <span class="btn">Get in Touch</span>
  </nav>
</header>
<div class="hero-copy">
  <h1>Building Your Financial Future with Confidence</h1>
  <p>Expert financial guidance tailored to your unique goals. We help individuals and businesses navigate complex financial decisions with clarity and confidence.</p>
  <div class="hero-btns"><span class="btn">Schedule a Consultation</span><span class="btn-ghost"></span></div>
</div>

<div class="abs about-panel"></div>
<div class="abs about-copy">
  <span class="tag">About Homes by Marlowe</span>
  <h2>Your Trusted Partner in Financial Success</h2>
  <p>At KRV•DEL, we believe that everyone deserves access to expert financial guidance. With over two decades of combined experience, our team of certified financial advisors is dedicated to helping you achieve your financial goals, whether you're planning for retirement, growing your wealth, or securing your family's future.</p>
  <p>We take a personalized approach to financial planning, understanding that each client's situation is unique. Our commitment to transparency, integrity, and client-focused service has made us a trusted name in financial advisory.</p>
  <div class="stats">
    <div class="stat">
      <svg width="22" height="22" viewBox="0 0 24 24" fill="none" stroke="#0f9488" stroke-width="2"><circle cx="12" cy="8" r="6"/><path d="M8.5 13L7 22l5-3 5 3-1.5-9"/></svg>
      <b>20+ Years</b><span>Experience</span>
    </div>
    <div class="stat">
      <svg width="22" height="22" viewBox="0 0 24 24" fill="none" stroke="#0f9488" stroke-width="2"><circle cx="9" cy="7" r="4"/><path d="M2 21v-2a5 5 0 0 1 5-5h4a5 5 0 0 1 5 5v2M16 3.1a4 4 0 0 1 0 7.8M22 21v-2a4 4 0 0 0-3-3.8"/></svg>
      <b>500+ Clients</b><span>Served</span>
    </div>
    <div class="stat">
      <svg width="22" height="22" viewBox="0 0 24 24" fill="none" stroke="#0f9488" stroke-width="2"><path d="M22 7l-8.5 8.5-5-5L2 17M16 7h6v6"/></svg>
      <b>$100M+</b><span>Assets Managed</span>
    </div>
  </div>
</div>
<div class="abs about-img" role="img" aria-label="Photo of a modern home office desk with a laptop against a teal wall"></div>
<div class="abs quote-box">"Excellence in financial advisory since 2004"</div>

<div class="abs services-head">
  <span class="tag">Our Services</span>
  <h2 class="section-title">Comprehensive Financial Solutions</h2>
  <p>We offer a full spectrum of financial advisory services designed to address every aspect of your financial life.</p>
</div>

<div class="card" style="left:76px;top:1853px;height:291px">
  <div class="icon-box"><svg width="20" height="20" viewBox="0 0 24 24" fill="none" stroke="#0f9488" stroke-width="2"><path d="M22 7l-8.5 8.5-5-5L2 17M16 7h6v6"/></svg></div>
  <h3>Investment Planning</h3>
  <p>Strategic portfolio management designed to grow your wealth while managing risk according to your comfort level and timeline.</p>
</div>
<div class="card" style="left:435px;top:1853px;height:291px">
  <div class="icon-box"><svg width="20" height="20" viewBox="0 0 24 24" fill="none" stroke="#0f9488" stroke-width="2"><path d="M12 22s8-4 8-10V5l-8-3-8 3v7c0 6 8 10 8 10z"/></svg></div>
  <h3>Retirement Planning</h3>
  <p>Comprehensive retirement strategies to ensure you can enjoy your golden years with financial security and peace of mind.</p>
</div>
<div class="card" style="left:794px;top:1853px;height:291px">
  <div class="icon-box"><svg width="20" height="20" viewBox="0 0 24 24" fill="none" stroke="#0f9488" stroke-width="2"><path d="M5 11a7 6 0 0 1 13-2h2v4l-2 1-1 3h-3v-2h-4v2H7l-1-3a5 5 0 0 1-1-3z"/><circle cx="15" cy="10" r=".5"/></svg></div>
  <h3>Wealth Management</h3>
  <p>Holistic wealth management services that encompass investment, tax, estate planning, and legacy preservation.</p>
</div>
<div class="card" style="left:76px;top:2174px;height:270px">
  <div class="icon-box"><svg width="20" height="20" viewBox="0 0 24 24" fill="none" stroke="#0f9488" stroke-width="2"><path d="M3 10l9-7 9 7v11H3z"/><path d="M9 21v-7h6v7"/></svg></div>
  <h3>Estate Planning</h3>
  <p>Protect your assets and provide for your loved ones with thoughtful estate planning and succession strategies.</p>
</div>
<div class="card" style="left:435px;top:2174px;height:270px">
  <div class="icon-box"><svg width="20" height="20" viewBox="0 0 24 24" fill="none" stroke="#0f9488" stroke-width="2"><rect x="3" y="7" width="18" height="14" rx="1"/><path d="M8 7V4h8v3M9 7v14M15 7v14"/></svg></div>
  <h3>Business Financial Advisory</h3>
  <p>Expert guidance for business owners on growth strategies, succession planning, and corporate financial management.</p>
</div>
<div class="card" style="left:794px;top:2174px;height:270px">
  <div class="icon-box"><svg width="20" height="20" viewBox="0 0 24 24" fill="none" stroke="#0f9488" stroke-width="2"><path d="M2 9l10-5 10 5-10 5z"/><path d="M6 11v5c3 2 9 2 12 0v-5"/></svg></div>
  <h3>Education Planning</h3>
  <p>Smart savings strategies to fund your children's education without compromising your other financial goals.</p>
</div>

<div class="abs approach"></div>
<div class="abs approach-img" role="img" aria-label="Abstract image of glowing red and green light lines"></div>
<div class="abs approach-copy">
  <span class="tag">Our Approach</span>
  <h2>A Proven Process for Financial Success</h2>
  <p class="lead">Our four-step approach ensures that every aspect of your financial life is carefully considered and optimized for your success.</p>
</div>
<div class="step" style="top:2795px"><div class="num">01</div><div><h4>Discovery &amp; Assessment</h4><p>We begin by understanding your current financial situation, goals, and concerns through in-depth consultations.</p></div></div>
<div class="step" style="top:2900px"><div class="num">02</div><div><h4>Strategy Development</h4><p>Our team creates a customized financial plan tailored to your unique objectives and risk tolerance.</p></div></div>
<div class="step" style="top:3006px"><div class="num">03</div><div><h4>Implementation</h4><p>We put your plan into action, coordinating all aspects of your financial strategy with precision and care.</p></div></div>
<div class="step" style="top:3113px"><div class="num">04</div><div><h4>Ongoing Review</h4><p>Regular reviews and adjustments ensure your plan evolves with your life changes and market conditions.</p></div></div>
<div class="abs fiduciary">
  <svg width="22" height="22" viewBox="0 0 24 24" fill="none" stroke="#14b8a6" stroke-width="2" style="flex:none;margin-top:2px"><circle cx="12" cy="12" r="9"/><path d="M8 12l3 3 5-6"/></svg>
  <div><h4>Fiduciary Commitment</h4><p>We are legally and ethically bound to act in your best interest at all times. Your success is our success.</p></div>
</div>

<div class="abs testi-bg"></div>
<div class="abs testi-head">
  <span class="tag">Client Testimonials</span>
  <h2 class="section-title">What Our Clients Say</h2>
  <p>Don't just take our word for it. Here's what our clients have to say about their experience working with KRV•DEL.</p>
</div>
<div class="tcard" style="left:76px">
  <div class="stars">
    <svg width="100" height="16" viewBox="0 0 100 16" fill="#14b8a6"><g id="st"><path d="M8 1l2.2 4.6 5 .7-3.6 3.5.9 5L8 12.4 3.5 14.8l.9-5L.8 6.3l5-.7z"/></g><use href="#st" x="21"/><use href="#st" x="42"/><use href="#st" x="63"/><use href="#st" x="84"/></svg>
  </div>
  <blockquote>"KRV•DEL transformed how I think about my business finances. Their strategic guidance helped me plan for growth while securing my family's future. The team is professional, knowledgeable, and genuinely cares about my success."</blockquote>
  <hr><div class="name">Lena Hartwell</div><div class="role">Small Business Owner</div>
</div>
<div class="tcard" style="left:435px">
  <div class="stars"><svg width="100" height="16" viewBox="0 0 100 16" fill="#14b8a6"><use href="#st"/><use href="#st" x="21"/><use href="#st" x="42"/><use href="#st" x="63"/><use href="#st" x="84"/></svg></div>
  <blockquote style="height:152px">"After years of uncertainty about retirement, the team at KRV•DEL gave me a clear, actionable plan. I now have peace of mind knowing my retirement is secure and I can enjoy this chapter of my life."</blockquote>
  <hr><div class="name">Owen Pratley</div><div class="role">Retired Educator</div>
</div>
<div class="tcard" style="left:794px">
  <div class="stars"><svg width="100" height="16" viewBox="0 0 100 16" fill="#14b8a6"><use href="#st"/><use href="#st" x="21"/><use href="#st" x="42"/><use href="#st" x="63"/><use href="#st" x="84"/></svg></div>
  <blockquote>"Working with KRV•DEL has been one of the best decisions I've made. They helped me consolidate my investments, reduce fees, and create a comprehensive financial plan that actually makes sense. Highly recommend!"</blockquote>
  <hr><div class="name">Marisol Quintero</div><div class="role">Healthcare Professional</div>
</div>

<div class="abs contact-copy">
  <span class="tag">Get In Touch</span>
  <h2>Let's Start Your Financial Journey</h2>
  <p class="lead">Ready to take control of your financial future? Schedule a complimentary consultation with one of our experienced advisors. We're here to answer your questions and help you create a plan that works for you.</p>
  <div class="info"><div class="ic"><svg width="18" height="18" viewBox="0 0 24 24" fill="none" stroke="#0f9488" stroke-width="2"><path d="M22 16.9v3a2 2 0 0 1-2.2 2A19.8 19.8 0 0 1 2.1 4.2 2 2 0 0 1 4.1 2h3a2 2 0 0 1 2 1.7l.5 3a2 2 0 0 1-.6 1.8L7.6 9.9a16 16 0 0 0 6.5 6.5l1.4-1.4a2 2 0 0 1 1.8-.6l3 .5a2 2 0 0 1 1.7 2z"/></svg></div><div><b>Phone</b><span>+1 (555) 204-3187</span></div></div>
  <div class="info"><div class="ic"><svg width="18" height="18" viewBox="0 0 24 24" fill="none" stroke="#0f9488" stroke-width="2"><rect x="2" y="4" width="20" height="16" rx="2"/><path d="M22 6l-10 7L2 6"/></svg></div><div><b>Email</b><span>info@krvdel.com</span></div></div>
  <div class="info"><div class="ic"><svg width="18" height="18" viewBox="0 0 24 24" fill="none" stroke="#0f9488" stroke-width="2"><path d="M20 10c0 6-8 12-8 12s-8-6-8-12a8 8 0 0 1 16 0z"/><circle cx="12" cy="10" r="3"/></svg></div><div><b>Office</b><span>Harbor Point &amp; Westvale, CA<br>United States</span></div></div>
</div>
<div class="abs hours">
  <h4>Office Hours</h4>
  <p>Monday - Friday: 9:00 AM - 5:00 PM<br>Saturday: By Appointment<br>Sunday: Closed</p>
</div>
<form class="abs form">
  <h3>Send Us a Message</h3>
  <div class="field"><label>Full Name</label><div class="input">Jordan Avery</div></div>
  <div class="field"><label>Email Address</label><div class="input">jordan@example.com</div></div>
  <div class="field"><label>Phone Number</label><div class="input">(123) 456-7890</div></div>
  <div class="field"><label>Message</label><div class="input area">Tell us about your financial goals and how we can help...</div></div>
  <span class="btn">Schedule Consultation</span>
</form>

<footer class="abs footer">
  <div class="abs f-brand">
    <div class="logo"><span class="dot"></span>Marlowe</div>
    <p>Building financial futures with confidence and integrity since 2004.</p>
    <div class="socials"><span></span><span></span><span></span></div>
  </div>
  <div class="abs f-col" style="left:346px"><h4>Quick Links</h4><a>About Us</a><a>Services</a><a>Our Approach</a><a>Testimonials</a></div>
  <div class="abs f-col" style="left:626px"><h4>Services</h4><a>Investment Planning</a><a>Retirement Planning</a><a>Wealth Management</a><a>Estate Planning</a></div>
  <div class="abs f-col" style="left:906px"><h4>Contact</h4><a>+1 (555) 204-3187</a><a>info@krvdel.com</a><a class="dim">Harbor Point &amp; Westvale, CA<br>United States</a></div>
  <div class="abs f-bottom">
    <span>© 2025 Homes by Marlowe. All rights<br>reserved.</span>
    <nav><span>Privacy Policy</span><span>Terms of Service</span><span>Disclaimer</span></nav>
  </div>
</footer>

</body>
</html>
```